Emergency and Referral Vet Hospital promotional sticker design

We're looking at getting some stickers designed that we could give to clients to put on their cars for promotion and advertising. If they could also be suitable for a goodie bag for conference too that would be great. I like the look of water-colour backgrounds, we'll need to include our logo and probably our address (Unit 4/372 Tarvenny Drive Success). We also have a hospital motto "... because they're family" if that could somehow be integrated, we only care for small animals (dogs, cats etc) but the design is very open to suggestion. Would love to see what you can create.

Industry/Entity Type

Veterinary

Colors
0054AA
0677BA
7BADD7
CADEEF
E8F1F8
0094D4
00A9DD
6FCCEA
C7EBF8
E9F6FB

Requirements
Nice to have
• Think beach vibes, blues maybe paw print shapes etc

```html
<!DOCTYPE html>
<html lang="en">
<head>
<meta charset="utf-8">
<title>Tidewell Vet Hospital Sticker</title>
<link rel="stylesheet" href="https://fonts.googleapis.com/css2?family=Roboto:wght@400;500&family=Kaushan+Script&display=swap">
<style>
  :root {
    --mat: #e6e6e6;
    --sky: #00a3de;
    --ocean: #0677ba;
    --deep: #0054aa;
    --mist: #6fccea;
    --white: #ffffff;
  }
  * { margin: 0; padding: 0; box-sizing: border-box; }
  html, body { width: 1200px; height: 885px; overflow: hidden; background: var(--mat); }
  .sticker {
    position: absolute; left: 150px; top: 142px; width: 900px; height: 599px;
    overflow: hidden; background: var(--sky);
    font-family: "Roboto", Arial, sans-serif; color: var(--white);
  }
  .sticker__art { position: absolute; inset: 0; }
  .brand {
    position: absolute; left: 700px; top: 52px; transform: translateX(-50%);
    display: flex; flex-direction: column; align-items: center; gap: 8px;
  }
  .brand__dot { width: 34px; height: 34px; border-radius: 50%; border: 3px solid var(--white); }
  .brand__name { font-size: 24px; font-weight: 500; letter-spacing: 0.5px; }
  .motto { position: absolute; left: 705px; transform: translateX(-50%); text-align: center; white-space: nowrap; }
  .motto__lead { top: 160px; font-family: "Kaushan Script", cursive; font-size: 44px; }
  .motto__main { top: 232px; font-size: 98px; font-weight: 500; line-height: 1; }
  .address { position: absolute; left: 785px; top: 410px; transform: translateX(-50%); text-align: center; }
  .address__pin { display: block; margin: 0 auto 14px; width: 26px; height: 34px; }
  .address__text { font-size: 24px; line-height: 36px; font-weight: 500; white-space: nowrap; }
</style>
</head>
<body>
<main class="sticker">
  <svg class="sticker__art" viewBox="0 0 900 599" xmlns="http://www.w3.org/2000/svg">
    <defs>
      <linearGradient id="photo-tone" x1="0" y1="0" x2="0.6" y2="1">
        <stop offset="0" stop-color="#f7d08a"/>
        <stop offset="0.35" stop-color="#d58a3d"/>
        <stop offset="0.7" stop-color="#8a5a2c"/>
        <stop offset="1" stop-color="#4a4a22"/>
      </linearGradient>
    </defs>
    <polygon class="band band--deep" points="318,0 400,0 650,599 560,599" fill="var(--deep)"/>
    <polygon class="band band--ocean" points="340,0 370,0 610,599 580,599" fill="var(--ocean)" opacity="0.7"/>
    <polygon class="photo" role="img" aria-label="Photo of a smiling corgi and a tabby kitten sitting in grass at sunset"
      points="0,0 318,0 560,599 0,599" fill="url(#photo-tone)"/>
    <polygon class="band band--deep" points="810,0 845,0 900,120 900,200" fill="var(--deep)"/>
    <polygon class="band band--ocean" points="860,0 900,0 900,80" fill="var(--ocean)"/>
    <line x1="870" y1="0" x2="900" y2="70" stroke="var(--white)" stroke-width="2"/>
    <polygon class="band band--deep" points="540,400 560,400 625,599 605,599" fill="var(--deep)"/>
    <polygon class="band band--ocean" points="575,390 592,390 665,599 648,599" fill="var(--ocean)"/>
    <line x1="560" y1="410" x2="623" y2="599" stroke="var(--white)" stroke-width="2"/>
    <g class="hatch" stroke="var(--deep)" stroke-width="4">
      <line x1="490" y1="60" x2="518" y2="38"/>
      <line x1="498" y1="70" x2="526" y2="48"/>
      <line x1="506" y1="80" x2="534" y2="58"/>
    </g>
    <g class="hatch" stroke="var(--white)" stroke-width="4">
      <line x1="210" y1="540" x2="250" y2="512"/>
      <line x1="216" y1="552" x2="256" y2="524"/>
      <line x1="222" y1="564" x2="262" y2="536"/>
    </g>
  </svg>

  <div class="brand">
    <span class="brand__dot"></span>
    <span class="brand__name">Tidewell</span>
  </div>

  <p class="motto motto__lead">Because they’re</p>
  <p class="motto motto__main">Family</p>

  <div class="address">
    <svg class="address__pin" viewBox="0 0 24 32" xmlns="http://www.w3.org/2000/svg" aria-hidden="true">
      <path d="M12 1C6 1 2 5.5 2 11c0 7.5 10 20 10 20s10-12.5 10-20C22 5.5 18 1 12 1z" fill="var(--white)"/>
      <circle cx="12" cy="11" r="4" fill="var(--sky)"/>
    </svg>
    <p class="address__text">Unit 4/372 Tarvenny<br>Drive Success</p>
  </div>
</main>
</body>
</html>
```